Small business services company needs a flyer designed

We need a flyer designed for a small building services company who has multiple roles ie- Roof, gutter and pressure cleaning, small building maintenance and garden cleanups. The company is based in Far North Queensland (Australia) where it is a tropical climate with lots of trees and green areas.

I want the colours to be based on the Logo and business card colours which will be added.

The flyer will need to be changeable so I can create monthly specials ie- Roof Cleaning Special, Gutter Cleaning Special or Pressure Cleaning special.

The roles of the business will be as stated on the attached business card.

Good evening all designers, please find below an update for you all, I hope it may answer some questions you have.

'd like the flyer to be DL size and at present I don't have any photo's. But i'd be happy for you to source some from google. The pictures I'd like would be of gutter cleaning from a ladder, pressure washing roofs & driveways with the large round "flat surface cleaners". Possibly have split pictures of the pressure cleaning to show before and after. 
Far North Queensland is a very tropical environment that has lots of palm trees and rain forest. The climate is usually 30+ degrees C. Incorporating those colours with the logo colours I'd like. 

Hello all designers.

I have just uploaded some of my own job pictures. There is a before and an after picture. If you source any other pictures, I'd like to see a flat surface/ spinmaster cleaner in operation, either on a roof or a driveway.

My goal is for a single sided flyer with all the details from my business card to be on the flyer. 

Please remember the climate in my area is very tropical and usually 30+ degrees C. Never cold or snowing. So please have pictures to reflect.

Thanks for the designs.
Regards,Darren

Reason: hi all designers. I have extended the deadline by 3 days to accommodate all the designers who have only recently accepted the brief nest invites. I have had a lot of declines and want the best designs I can choice from. This is no reflection of the calibre of the designs I have already received. I look forward to seeing all the updates and new designs. Regards, Darren

Home owners who take pride in the street appeal of their homes, or to add value to their selling price when a house goes on the sales market.

Building

```html
<!DOCTYPE html>
<html lang="en">
<head>
<meta charset="utf-8">
<title>Upreach – Roof Cleaning Flyer</title>
<link href="https://fonts.googleapis.com/css2?family=Lato:ital,wght@0,400;0,700;0,900;1,400;1,700&display=swap" rel="stylesheet">
<style>
  :root {
    --navy: #2b3990;
    --teal: #00a99d;
    --photo-grey: #d1d3d4;
    --paper: #f3f3f3;
    --white: #ffffff;
    --ink: #231f20;
  }
  * { margin: 0; padding: 0; box-sizing: border-box; }
  html, body { width: 846px; height: 1200px; overflow: hidden; background: var(--paper); }
  .flyer {
    position: relative;
    width: 846px;
    height: 1200px;
    background: var(--paper);
    font-family: "Lato", sans-serif;
    overflow: hidden;
  }
  .header-art { position: absolute; left: 0; top: 0; width: 846px; height: 1200px; }
  .photo-note {
    position: absolute; left: 0; top: 162px; width: 846px;
    text-align: center; font-size: 22px; color: var(--ink);
  }
  .special-title {
    position: absolute; left: 0; top: 482px; width: 846px;
    text-align: center; color: var(--white);
    font-size: 68px; font-weight: 900; letter-spacing: 0.5px;
  }
  .service {
    position: absolute; width: 353px; height: 67px;
    background: var(--navy); border: 4px solid var(--teal); border-radius: 11px;
    color: var(--white); display: flex; flex-direction: column; justify-content: center;
    font-size: 23.5px; font-weight: 700; line-height: 1.12;
  }
  .service--left { left: 55px; padding-left: 33px; text-align: left; }
  .service--right { left: 437px; padding-right: 33px; text-align: right; }
  .service--row1 { top: 629px; }
  .service--row2 { top: 715px; }
  .service__note { font-size: 14px; font-weight: 400; font-style: italic; margin-top: 1px; }
  .credentials {
    position: absolute; left: 0; top: 803px; width: 846px;
    text-align: center; color: var(--teal);
    font-size: 22.5px; font-weight: 700; font-style: italic; line-height: 36px;
  }
  .contact { position: absolute; left: 56px; top: 1036px; }
  .contact__row { display: flex; height: 42px; align-items: center; font-size: 22px; }
  .contact__label { width: 84px; color: var(--teal); font-weight: 700; font-style: italic; }
  .contact__value { color: var(--navy); font-weight: 400; }
  .brand {
    position: absolute; left: 470px; top: 1058px; width: 320px; height: 70px;
    display: flex; align-items: center; justify-content: center; gap: 14px;
  }
  .brand__dot { width: 26px; height: 26px; border-radius: 50%; background: var(--teal); }
  .brand__name { font-size: 54px; font-weight: 900; color: var(--navy); letter-spacing: 1px; }
</style>
</head>
<body>
<div class="flyer">
  <svg class="header-art" viewBox="0 0 1000 1419" preserveAspectRatio="none" aria-hidden="true">
    <defs>
      <filter id="soft-shadow" x="-10%" y="-200%" width="120%" height="500%">
        <feGaussianBlur stdDeviation="6"/>
      </filter>
    </defs>
    <ellipse cx="500" cy="683" rx="420" ry="8" fill="#9a9a9a" opacity="0.55" filter="url(#soft-shadow)"/>
    <rect class="title-band" x="65" y="300" width="870" height="375" rx="16" fill="var(--navy)" stroke="var(--teal)" stroke-width="5"/>
    <path d="M0,0 H1000 V290 Q520,672 0,415 Z" fill="var(--teal)"/>
    <path d="M0,0 H1000 V240 Q520,678 0,385 Z" fill="var(--white)"/>
    <path d="M0,0 H1000 V215 Q520,664 0,370 Z" fill="var(--navy)"/>
    <path d="M0,0 H1000 V205 Q520,642 0,310 Z" fill="var(--photo-grey)" role="img" aria-label="Monthly special photo: roof, gutter or pressure cleaning job"/>
  </svg>

  <p class="photo-note">[Photo Here: According to monthly special]</p>

  <h1 class="special-title">ROOF CLEANING</h1>

  <div class="service service--left service--row1">Gutter Cleaning</div>
  <div class="service service--right service--row1">Minor Roof, Gutter<br>&amp; Building Maintenance</div>
  <div class="service service--left service--row2">Pressure Cleaning<span class="service__note">Roofs, Driveways, etc.</span></div>
  <div class="service service--right service--row2">Garden Waste Removal<br>&amp; Complex Cleanups</div>

  <div class="credentials">
    <p>Residential, Commercial &amp; Body Corporate Jobs</p>
    <p>National Working at Heights Certification</p>
    <p>10% Discount for Emergency Services, Defence &amp; Seniors</p>
  </div>

  <div class="contact">
    <div class="contact__row"><span class="contact__label">Tel:</span><span class="contact__value">0400 555 127</span></div>
    <div class="contact__row"><span class="contact__label">E-mail:</span><span class="contact__value">roofcare@coastnet.com.au</span></div>
    <div class="contact__row"><span class="contact__label">ABN:</span><span class="contact__value">52 804 219 307</span></div>
  </div>

  <div class="brand">
    <span class="brand__dot"></span>
    <span class="brand__name">UPREACH</span>
  </div>
</div>
</body>
</html>
```